Corvale Homes

To produce a business card design for our newly established house building and development company, We have had a logo design done please see attached, our slogan is "building your home sweet home"
Contact Information for Business Card
Adress on card needs to Read - 58 Elmsworth Lane, Kettering, Northamptonshire NN16 4QT. Director name Dean Vascotti
Requirements
Must have
- Web adress is www.corvale-homes.co.uk
- Email address is info@corvale-homes.co.uk
- phone number 07700 900417

```html
<!DOCTYPE html>
<html lang="en">
<head>
<meta charset="utf-8">
<title>Corvale Homes – Business Card</title>
<link rel="stylesheet" href="https://fonts.googleapis.com/css2?family=Roboto:wght@400;500;700&display=swap">
<style>
  :root {
    --backdrop: #3b3330;
    --card: #1c1e20;
    --green: #7dc242;
    --grey: #9a9a9a;
    --white: #f2f2f2;
    --rule: #e6e6e6;
  }
  * { margin: 0; padding: 0; box-sizing: border-box; }
  html, body {
    width: 1200px; height: 769px; overflow: hidden;
    background: var(--backdrop);
    font-family: "Roboto", Arial, sans-serif;
  }
  .sheet {
    width: 1200px; height: 769px;
    display: flex; align-items: center; justify-content: center; gap: 50px;
  }
  .card {
    position: relative;
    width: 520px; height: 297px;
    background: var(--card);
    border-radius: 3px;
    box-shadow: 0 10px 30px rgba(0,0,0,.45);
  }
  /* front */
  .front .brand-name {
    position: absolute; left: 0; right: 0; top: 112px;
    text-align: center;
    font-size: 34px; font-weight: 700; color: var(--green);
    letter-spacing: 1px;
  }
  .front .web {
    position: absolute; left: 0; right: 0; top: 186px;
    text-align: center;
    font-size: 12px; color: var(--grey);
    letter-spacing: 3px; text-transform: uppercase;
  }
  /* back */
  .back .brand-name {
    position: absolute; right: 30px; top: 92px;
    font-size: 22px; font-weight: 700; color: var(--green);
    text-transform: uppercase; letter-spacing: .5px;
  }
  .back .person { position: absolute; left: 38px; top: 112px; }
  .back .person-name {
    font-size: 17px; font-weight: 500; color: var(--green);
    text-transform: uppercase; line-height: 1.1;
  }
  .back .person-role {
    font-size: 12px; font-weight: 500; color: var(--white);
    text-transform: uppercase; margin-top: 2px;
  }
  .back .divider {
    position: absolute; left: 36px; right: 40px; top: 165px;
    height: 1px; background: var(--rule);
  }
  .back .contacts {
    position: absolute; left: 38px; top: 178px;
    list-style: none;
  }
  .back .contacts li {
    display: flex; align-items: center; gap: 8px;
    font-size: 12px; color: var(--white); line-height: 19px;
  }
  .back .contacts svg { width: 10px; height: 10px; fill: var(--green); flex: none; }
  .back .address {
    position: absolute; right: 40px; bottom: 30px;
    font-style: normal; text-align: left;
    font-size: 13px; color: var(--white); line-height: 18px;
  }
</style>
</head>
<body>
<main class="sheet">
  <section class="card front">
    <div class="brand-name">Corvale Homes</div>
    <div class="web">www.corvale-homes.co.uk</div>
  </section>

  <section class="card back">
    <div class="brand-name">Corvale Homes</div>
    <div class="person">
      <div class="person-name">Dean Vascotti</div>
      <div class="person-role">Director</div>
    </div>
    <div class="divider"></div>
    <ul class="contacts">
      <li>
        <svg viewBox="0 0 10 10" aria-hidden="true"><path d="M2 0.5 L3.6 2.8 L2.7 3.8 Q3.6 5.9 6.2 7.3 L7.2 6.4 L9.5 8 L8.3 9.6 Q4.6 9.5 1.8 6.6 Q0.3 4.6 0.4 1.7 Z"/></svg>
        07700 900417
      </li>
      <li>
        <svg viewBox="0 0 10 10" aria-hidden="true"><path d="M0.5 2 H9.5 V8.5 H0.5 Z M1.2 2.6 L5 5.4 L8.8 2.6 V2.6 Z" fill-rule="evenodd"/></svg>
        info@corvale-homes.co.uk
      </li>
      <li>
        <svg viewBox="0 0 10 10" aria-hidden="true"><circle cx="5" cy="5" r="4.6"/></svg>
        www.corvale-homes.co.uk
      </li>
    </ul>
    <address class="address">
      58 Elmsworth Lane, Kettering<br>
      Northamptonshire NN16 4QT
    </address>
  </section>
</main>
</body>
</html>
```